Indian Takeaway Menu

We need a flyer for an existing Indian Takeaway business in dublin Ireland.

We need some upto date style menu may be a A4 sheet folded in 3 layers.

But not folded in landscape side folded from portrait side and typing from portrait side from top, as we type in a word document and then fold the letter in 3 layers.
please amend your designs as everyone have done the same thing which is very boring.

We have a logo we would like to use in front of the menu. Designer have to come up with the colour which will help the logo to stand out. we also have a review in the paper which we would like to use at the back page somewhere.

New ideas are welcome from the designer
Please look at the example menu attached.

City population

Landscape

Font styles to use
Sans Serif

Colors
acd037

Requirements
Must have
• ingredient sign for
• Nuts
• Celiac
• Low fat
• Diary
Nice to have
• attractive

```html
<!DOCTYPE html>
<html lang="en">
<head>
<meta charset="utf-8">
<title>Saffron Hearth – Takeaway Menu</title>
<link rel="stylesheet" href="https://fonts.googleapis.com/css2?family=Arimo:ital,wght@0,400;0,700;1,400&display=swap">
<style>
  :root{
    --paper:#ffffff;
    --ink:#1d1d1d;
    --muted:#444444;
    --brand:#a8241f;
    --accent:#acd037;
    --ornament:#3a3a3a;
    --chili-mild:#8bb43a;
    --chili-medium:#e39a1f;
    --chili-hot:#c8261c;
    --badge:#6d6d6d;
  }
  *{margin:0;padding:0;box-sizing:border-box}
  html,body{width:849px;height:1200px;overflow:hidden;background:var(--paper)}
  body{font-family:"Arimo",Arial,sans-serif;color:var(--ink);position:relative}
  .frame{position:absolute;left:40px;right:40px;top:40px;height:300px;border:1px solid var(--ornament);border-bottom:none}
  .ornament{position:absolute;background:linear-gradient(135deg,#4a4a4a,#1f1f1f);border-radius:40% 10% 40% 10%}
  .ornament.tl{left:12px;top:12px;width:86px;height:86px}
  .ornament.tr{right:12px;top:12px;width:86px;height:86px}
  .ornament.bl{left:12px;top:280px;width:72px;height:62px}
  .ornament.br{right:12px;top:280px;width:72px;height:62px}

  .masthead{position:absolute;left:0;right:0;top:34px;text-align:center}
  .brand-mark{width:34px;height:34px;border-radius:50%;background:var(--accent);margin:0 auto 10px}
  .brand-name{font-weight:700;font-size:66px;color:var(--brand);line-height:1;letter-spacing:1px}
  .tagline{font-size:26px;margin-top:26px}
  .note{font-size:15px;margin-top:12px}
  .web{font-size:15px;color:var(--brand);margin-top:4px}
  .phone{font-size:24px;margin-top:10px}
  .hours{font-size:22px;line-height:1.25;margin-top:4px}
  .hours .indent{padding-left:120px;display:block}

  .col{position:absolute;top:430px}
  .col h2{font-size:22px;font-weight:400;display:flex;align-items:center;gap:10px;height:26px;margin-bottom:12px}
  .deals{left:20px;width:270px}
  .sets{left:310px;width:135px}
  .sets-more{left:560px;width:265px;top:438px}

  .item{margin-bottom:5px}
  .item-head{display:flex;justify-content:space-between;font-size:11px;line-height:13px;font-weight:700;color:var(--brand)}
  .item-head .price{color:var(--ink);font-weight:400}
  .desc{font-size:9px;line-height:11px;font-style:italic;color:var(--muted);width:220px}
  .set{margin-bottom:18px}
  .set .item-head{font-size:9.5px;line-height:12px}
  .set .sub{font-size:10px;color:var(--muted);margin-bottom:8px}
  .set ul{list-style:none;font-size:8.5px;font-style:italic;color:var(--muted);line-height:10.5px}
  .sets-more .set{margin-bottom:22px}

  .legend{position:absolute;left:20px;top:650px;list-style:none}
  .legend li{display:flex;align-items:center;gap:22px;height:48px;font-size:19px}
  .legend .key{width:34px;height:34px;border:2px solid var(--ink);border-radius:8px;display:flex;align-items:center;justify-content:center;font-size:15px;font-weight:700}
  .legend .key.round{border-radius:50%}
  .legend svg{width:34px;height:24px}

  .tag{display:inline-flex;width:24px;height:24px;border:1.5px solid var(--ink);border-radius:5px;font-size:10px;font-weight:700;align-items:center;justify-content:center}

  .badge{position:absolute;width:180px;height:180px;border-radius:50%;background:radial-gradient(circle,#9a9a9a 0 45%,var(--badge) 46% 100%);border:3px solid #4f4f4f}
</style>
</head>
<body>
  <div class="frame"></div>
  <div class="ornament tl" role="img" aria-label="Decorative elephant ornament"></div>
  <div class="ornament tr" role="img" aria-label="Decorative elephant ornament"></div>
  <div class="ornament bl" role="img" aria-label="Decorative elephant ornament"></div>
  <div class="ornament br" role="img" aria-label="Decorative elephant ornament"></div>

  <header class="masthead">
    <div class="brand-mark"></div>
    <div class="brand-name">Saffron Hearth</div>
    <div class="tagline">Authentic Indian Takeaway</div>
    <div class="note">All our meals are cooked to order.</div>
    <div class="web">www.saffronhearth.ie</div>
    <div class="phone">015550142, 015550187</div>
    <div class="hours">Opening Hours: Sun to Thurs 5PM to 10.00PM
      <span class="indent">Fri to Sat 5.00PM-10.30PM</span>
      Deliveries From 5.30PM</div>
  </header>

  <section class="col deals">
    <h2>Meal Deals <span class="tag">LF</span></h2>
    <div class="item"><div class="item-head"><span>CHICKEN DUPIAZA</span><span class="price">€6.00</span></div><p class="desc">Chicken breast pieces cooked with fresh tomatoes and sliced onions</p></div>
    <div class="item"><div class="item-head"><span>CHICKEN ROGAN JOSH</span><span class="price">€6.00</span></div><p class="desc">A rich chicken curry prepared with fresh herbs &amp; spices, a delicacy from Kashmir</p></div>
    <div class="item"><div class="item-head"><span>CHICKEN MADRAS</span><span class="price">€6.00</span></div><p class="desc">Chicken cooked in a hot spicy sauce</p></div>
    <div class="item"><div class="item-head"><span>TARKARI MARRANI</span><span class="price">€6.00</span></div><p class="desc">Mixed seasonal vegetables in a smooth butter, cream and tomato sauce</p></div>
    <div class="item"><div class="item-head"><span>ALOO CHICKEN</span><span class="price">€6.00</span></div><p class="desc">Chicken cooked with spiced potatoes and roasted cumin</p></div>
  </section>

  <section class="col sets">
    <h2>Set Meals</h2>
    <div class="set">
      <div class="item-head"><span>SET MEAL FOR 1</span><span class="price">€14.00</span></div>
      <div class="sub">Vegetarian</div>
      <ul><li>Onion Bhajee</li><li>Seasonal vegetable curry</li><li>Pilau rice</li><li>Naan</li><li>Poppadums &amp; spiced onion</li><li>Soft Drink</li></ul>
    </div>
    <div class="set">
      <div class="item-head"><span>SET MEAL FOR 1</span><span class="price">€16.00</span></div>
      <div class="sub">Non Vegetarian</div>
      <ul><li>Chicken tikka</li><li>Chicken tikka masala</li><li>Pilau rice</li><li>Naan</li><li>Poppadums &amp; spiced onion</li><li>Soft Drink</li></ul>
    </div>
  </section>

  <section class="col sets-more">
    <div class="set">
      <div class="item-head"><span>SET MEAL 5</span><span class="price">€35.00</span></div>
      <ul><li>Onion Bhajee</li><li>Chicken tikka</li><li>Chicken tikka masala</li><li>Lamb Rogan Josh</li><li>2 x Pilau rice</li><li>Naan</li><li>Poppadums &amp; spiced onion</li><li>2 Soft Drinks</li></ul>
    </div>
    <div class="set">
      <div class="item-head"><span>SET MEAL FOR 2 OR 4</span><span class="price">€39.00</span></div>
      <ul><li>Onion Bhajee</li><li>Vegetable samosa</li><li>Chicken tikka</li><li>Chicken Tikka Masala</li><li>Lamb Rogan Josh</li><li>Seasonal Vegetable Curry</li><li>2 x Pilau rice</li><li>Naan</li><li>Poppadums &amp; spiced onion</li><li>2 Soft Drinks</li></ul>
    </div>
  </section>

  <ul class="legend">
    <li><span class="key">D</span>Dairy</li>
    <li><span class="key round">N</span>Nuts</li>
    <li><span class="key round">CL</span>Celiac</li>
    <li><span class="key">LF</span>Low Fat</li>
    <li><svg viewBox="0 0 40 24"><path d="M4 12 Q20 2 36 10 Q20 20 4 12Z" fill="var(--chili-mild)"/></svg>Mildly Spicy</li>
    <li><svg viewBox="0 0 40 24"><path d="M4 12 Q20 2 36 10 Q20 20 4 12Z" fill="var(--chili-medium)"/></svg>Medium Spicy</li>
    <li><svg viewBox="0 0 40 24"><path d="M4 12 Q20 2 36 10 Q20 20 4 12Z" fill="var(--chili-hot)"/></svg>Hot</li>
  </ul>

  <div class="badge" style="left:610px;top:700px" role="img" aria-label="Award badge"></div>
  <div class="badge" style="left:600px;top:800px" role="img" aria-label="Award badge"></div>
  <div class="badge" style="left:610px;top:900px" role="img" aria-label="Award badge"></div>
</body>
</html>
```